Website for BQM CIVIL

looking for a clean crisp website outlining what we do, we are a telecommunications cable installer working on internet cabling, i am just looking for imagery and we will complete content

i need a

home page template
services tab (4 services)
Rod / Roping
Hauling
Civil
Surveying
Contact Us Page
Testimonials Page
About Us
Our Vision
History

Target Market(s)

Telecommunication Companies

Industry/Entity Type

Telecommunications

Requirements
Must have
• images and logo themed colors

this is main project we are working on

http://www.vorlyx.com.au/

this is an example of our competitor site in the same field, we are much smaller though

```html
<!DOCTYPE html>
<html lang="en">
<head>
<meta charset="utf-8">
<title>BQM CIVIL – Home</title>
<link rel="stylesheet" href="https://fonts.googleapis.com/css2?family=PT+Sans+Narrow:wght@400;700&family=Source+Sans+3:wght@400;600&display=swap">
<style>
:root{
  --orange:#f7770f;
  --orange-light:#ff9a2e;
  --navy:#1f3560;
  --navy-dark:#172746;
  --hero-top:#2c4c82;
  --hero-bottom:#243f6d;
  --blue-title:#2a6db3;
  --text:#4a4a4a;
  --text-dark:#333;
  --page:#f4f4f4;
  --card-border:#d8d8d8;
  --footer:#1c1c1e;
  --footer-text:#d9d9d9;
  --white:#fff;
}
*{box-sizing:border-box;margin:0;padding:0}
html,body{width:1108px;height:1200px;overflow:hidden}
body{position:relative;background:var(--page);font-family:"Source Sans 3",Arial,sans-serif;color:var(--text)}
.abs{position:absolute}
.narrow{font-family:"PT Sans Narrow","Arial Narrow",sans-serif}

/* header */
.site-header{left:0;top:0;width:1108px;height:120px;background:linear-gradient(#fff 0,#fff 80px,#e6e7ea 120px)}
.brand{left:134px;top:30px;display:flex;align-items:center;gap:12px}
.brand-mark{width:30px;height:30px;background:var(--orange);border-radius:50%}
.brand-name{font-family:"PT Sans Narrow",sans-serif;font-weight:700;font-size:44px;color:var(--navy);letter-spacing:1px;line-height:1}
.search{left:712px;top:41px;display:flex;align-items:center}
.search-icon{width:23px;height:25px;background:var(--orange);border-radius:3px 0 0 3px;display:flex;align-items:center;justify-content:center}
.search-field{width:182px;height:25px;background:#ececec;border-radius:0 4px 4px 0}
.search-go{margin-left:9px;width:40px;height:22px;background:#111;color:#fff;border-radius:4px;font-size:12px;display:flex;align-items:center;justify-content:center}

/* nav */
.main-nav{left:0;top:120px;width:1108px;height:32px;background:linear-gradient(#2a3f66,var(--navy-dark));border-bottom:1px solid #4a6a5a}
.nav-home{left:134px;top:112px;width:87px;height:40px;background:var(--orange);color:#fff;font-size:14px;display:flex;align-items:center;justify-content:center;padding-top:8px}
.nav-item{top:125px;font-size:14px;color:#fff}

/* hero */
.hero{left:0;top:152px;width:1108px;height:343px;background:linear-gradient(var(--hero-top),var(--hero-bottom))}
.hero-base{left:0;top:495px;width:1108px;height:8px;background:#1d2f52}
.hero-shade{left:0;top:503px;width:1108px;height:40px;background:linear-gradient(#d9dadd,var(--page))}
.hero-photo{left:118px;top:176px;width:517px;height:292px;border:4px solid #fff;background:linear-gradient(110deg,#9aa3ad,#4d5560 45%,#c9ccd0 70%,#2a2d33);box-shadow:0 14px 18px -10px rgba(0,0,0,.55)}
.hero-title{left:664px;top:212px;font-size:19px;font-weight:700;color:#fff}
.hero-copy{left:662px;top:254px;width:325px;font-size:12.5px;line-height:19.4px;color:#e3e9f3}
.btn{background:linear-gradient(var(--orange-light),var(--orange));color:#fff;display:flex;align-items:center;justify-content:center;border-radius:8px;box-shadow:2px 3px 4px rgba(0,0,0,.35)}
.hero-more{left:668px;top:374px;width:133px;height:34px;font-size:19px;font-weight:700;border-radius:12px}
.arrow{width:56px;height:56px;border-radius:50%;background:#0c0c0c;border:2px solid #333;display:flex;align-items:center;justify-content:center}

/* services */
.section-title{left:101px;top:538px;font-size:17px;font-weight:700;color:var(--text-dark)}
.card{top:574px;width:214px;height:201px;background:#fff;border:1px solid var(--card-border);border-radius:3px;box-shadow:0 10px 8px -8px rgba(0,0,0,.35)}
.card-title{position:absolute;left:15px;top:6px;font-size:19px;color:var(--blue-title)}
.card-frame{position:absolute;left:12px;top:32px;width:190px;height:90px;background:#eee;border-radius:4px;padding:5px 8px}
.card-photo{width:100%;height:100%;border-radius:4px}
.card-text{position:absolute;left:15px;top:130px;width:184px;font-size:10.5px;line-height:14.8px;text-align:justify}
.card-more{position:absolute;right:14px;top:180px;font-size:10.5px;display:flex;align-items:center;gap:9px}

/* newsletter + welcome */
.block-title{font-size:20px;color:var(--blue-title)}
.newsletter-text{left:107px;top:844px;width:242px;font-size:10.5px;line-height:16.6px;text-align:justify}
.email{left:106px;top:906px;width:239px;height:29px;border:2px solid #ddd;background:#fff;font-size:10.5px;font-style:italic;color:#888;padding:6px 14px}
.subscribe{left:229px;top:954px;width:112px;height:30px;font-size:14px;font-weight:700;border-radius:2px;box-shadow:none}
.welcome-title{left:408px;top:818px;font-size:22px;color:var(--text-dark)}
.welcome-title span{color:var(--blue-title)}
.welcome-text{left:413px;top:852px;width:605px;font-size:10.6px;line-height:16.6px;color:#3c3c3c}
.welcome-text p+p{margin-top:16.6px}
.view-more{left:903px;top:982px;width:107px;height:34px;font-size:15px;border-radius:9px}

/* footer */
.site-footer{left:0;top:1035px;width:1108px;height:165px;background:var(--footer)}
.footer-links{top:1060px;list-style:none;font-size:11px;line-height:22.2px;color:var(--footer-text)}
.social{left:877px;top:1060px;display:flex;gap:14px}
.social span{width:21px;height:21px;border-radius:2px;background:#3a5a9a}
.social span:nth-child(2){background:#36a3d9}
.social span:nth-child(3){background:#2f6fa6}
.social span:nth-child(4){background:#ef8a1a}
.copyright{right:103px;top:1099px;font-size:11px;color:var(--footer-text);text-align:right;line-height:22.5px}
</style>
</head>
<body>

<header class="abs site-header"></header>
<div class="abs brand"><span class="brand-mark"></span><span class="brand-name">BQM CIVIL</span></div>
<form class="abs search">
  <span class="search-icon"><svg width="13" height="13" viewBox="0 0 13 13"><circle cx="5.5" cy="5.5" r="3.8" fill="none" stroke="#fff" stroke-width="1.8"/><line x1="8.3" y1="8.3" x2="12" y2="12" stroke="#fff" stroke-width="2"/></svg></span>
  <span class="search-field"></span>
  <span class="search-go">GO</span>
</form>

<nav class="abs main-nav"></nav>
<span class="abs nav-home">Home</span>
<span class="abs nav-item" style="left:243px">Services</span>
<span class="abs nav-item" style="left:338px">Testimonials</span>
<span class="abs nav-item" style="left:459px">About Us</span>
<span class="abs nav-item" style="left:559px">Our Vision</span>
<span class="abs nav-item" style="left:667px">History</span>
<span class="abs nav-item" style="left:757px">Contact Us</span>

<section class="abs hero"></section>
<div class="abs hero-base"></div>
<div class="abs hero-shade"></div>
<div class="abs hero-photo" role="img" aria-label="Technician with a laptop in a server room"></div>
<h1 class="abs hero-title narrow">LOREM IPSUM DOLOR SIT AMET, ELIT</h1>
<p class="abs hero-copy">Cum sociis natoque penatibus et magnis dis parturient montes, nascetur ridiculus mus. In iaculis facilisis massa. Etiam eu urna. Sed porta.Cum sociis natoque penatibus et magnis dis parturient montes, nascetur ridiculus mus. In iaculis facilisis massa. Etiam eu urna. Sed porta.</p>
<a class="abs btn hero-more narrow">MORE</a>
<span class="abs arrow" style="left:26px;top:286px"><svg width="14" height="18" viewBox="0 0 14 18"><path d="M10 2 3 9l7 7" fill="none" stroke="#fff" stroke-width="3.2"/></svg></span>
<span class="abs arrow" style="left:1015px;top:286px"><svg width="14" height="18" viewBox="0 0 14 18"><path d="M4 2l7 7-7 7" fill="none" stroke="#fff" stroke-width="3.2"/></svg></span>

<h2 class="abs section-title narrow">OUR SERVICES</h2>

<article class="abs card" style="left:103px">
  <h3 class="card-title narrow">Rod / Roping</h3>
  <div class="card-frame"><div class="card-photo" role="img" aria-label="Cable connectors in a rack" style="background:linear-gradient(160deg,#c9cbcf,#3a3c40 55%,#777a80)"></div></div>
  <p class="card-text">Sed ut perspiciatis unde omnis iste natus error sit voluptatem accusantium doloremque laudantium.</p>
  <span class="card-more">MORE <svg width="7" height="9"><path d="M0 0l7 4.5L0 9z" fill="#2a8ad1"/></svg></span>
</article>
<article class="abs card" style="left:334px">
  <h3 class="card-title narrow">Hauling</h3>
  <div class="card-frame"><div class="card-photo" role="img" aria-label="Office room with equipment" style="background:linear-gradient(#3d6a9c,#9db3c7 45%,#d7dbe0)"></div></div>
  <p class="card-text">Sed ut perspiciatis unde omnis iste natus error sit voluptatem accusantium doloremque laudantium.</p>
  <span class="card-more">MORE <svg width="7" height="9"><path d="M0 0l7 4.5L0 9z" fill="#2a8ad1"/></svg></span>
</article>
<article class="abs card" style="left:565px">
  <h3 class="card-title narrow">Civil</h3>
  <div class="card-frame"><div class="card-photo" role="img" aria-label="Communications tower against a blue sky" style="background:linear-gradient(#4d86c9,#6a9bd3 60%,#3e4b5c)"></div></div>
  <p class="card-text">Sed ut perspiciatis unde omnis iste natus error sit voluptatem accusantium doloremque laudantium.</p>
  <span class="card-more">MORE <svg width="7" height="9"><path d="M0 0l7 4.5L0 9z" fill="#2a8ad1"/></svg></span>
</article>
<article class="abs card" style="left:797px">
  <h3 class="card-title narrow">Surveying</h3>
  <div class="card-frame"><div class="card-photo" role="img" aria-label="Technicians working on network cabling" style="background:linear-gradient(90deg,#5b5148,#8a8d92 50%,#3a3633)"></div></div>
  <p class="card-text">Sed ut perspiciatis unde omnis iste natus error sit voluptatem accusantium doloremque laudantium.</p>
  <span class="card-more">MORE <svg width="7" height="9"><path d="M0 0l7 4.5L0 9z" fill="#2a8ad1"/></svg></span>
</article>

<h2 class="abs block-title narrow" style="left:105px;top:812px">Newsletter</h2>
<p class="abs newsletter-text">Sed ut perspiciatis unde omnis iste natus error sit voluptatem accusantium doloremque laudantium, totam rem aperiam.</p>
<div class="abs email">Your Email Id</div>
<a class="abs btn subscribe narrow">Subscribe</a>

<h2 class="abs welcome-title narrow">Welcome to <span>BQM</span></h2>
<div class="abs welcome-text">
  <p>Uenim ad minim veniam, quis laboris nisi utaliquip ex irurdolor into Uenim ad minim veniam, quis nostrud&nbsp; Uenim ad minim veniam, quis laboris nisi utaliquip ex irurdolor into Uenim adminim veniam, quis nostrud&nbsp; Uenim ad minim veniam, quis laboris nisi utaliquip ex irurdolor into Uenim ad minim veniam, quis nostrud Uenim ad minim veniam, quis laboris nisi utaliquip ex irurdolor into Uenim ad minim veniam, quis nostrud&nbsp; Uenim ad minim veniam, quis laboris nisi utaliquip ex irurdolor.</p>
  <p>Uenim ad minim veniam, quis laboris nisi utaliquip ex irurdolor into Uenim ad minim veniam, quis nostrud Uenim ad minim veniam, quis laboris nisi utaliquip ex irurdolor into Uenim ad minim veniam, quis nostrud&nbsp; Uenim ad minim veniam.</p>
</div>
<a class="abs btn view-more narrow">View More...</a>

<footer class="abs site-footer"></footer>
<ul class="abs footer-links" style="left:107px"><li>Home</li><li>Services</li><li>Contact Us</li><li>Testimonials</li><li>About Us</li></ul>
<ul class="abs footer-links" style="left:228px"><li>Our Vision</li><li>History</li><li>Privacy</li><li>Terms of use</li><li>Sitemap</li></ul>
<div class="abs social"><span></span><span></span><span></span><span></span></div>
<p class="abs copyright">Copyright ©&nbsp; 2013&nbsp; bqm civil. All rights reserved.<br>x2</p>

</body>
</html>
```